Business Card with PUNCH
bluepinelodge.net
Project: Business Card with PUNCH
Business Card with PUNCH - Consulting
Creative Brief
Simple
Morris Trulsow
President
418 Dunmere Lane Suite 207 Spring, TX 77291
morris@bluepinelodge.net
logo on the back please
mtrulsow mtrulsow
WOW, what a tremendous effort overnight! Here is what I can tell you from what we have seen so far: 1. Prefer horizontal orientation of card rather than vertical. 2. Prefer the white cards with the blue and gray logo vs. the darker colors 3. Would like the back of the card to be white with room for a hand written note 4. Clear plastic cards are not a hit 5. Not a fan of card that look like the data is presented on any kind of a 'tab' or website type icons. Thanks for the many creative ideas, we are excited about this contest. mt

```html
<!DOCTYPE html>
<html lang="en">
<head>
<meta charset="utf-8">
<title>Blue Pine Lodge business card</title>
<link href="https://fonts.googleapis.com/css2?family=Montserrat:wght@400;600;700&display=swap" rel="stylesheet">
<style>
  :root {
    --stage: #efefef;
    --card-white: #ffffff;
    --ink: #3a3a3a;
    --ink-soft: #6b6b6b;
    --brand-blue: #2a2f9e;
    --brand-blue-dark: #1c2078;
    --swoosh-gray: #c9cbd1;
    --on-dark: #ffffff;
  }
  html, body {
    margin: 0;
    width: 1200px;
    height: 939px;
    overflow: hidden;
    background: var(--stage);
    font-family: "Montserrat", Arial, sans-serif;
  }
  .stage {
    position: relative;
    width: 1200px;
    height: 939px;
  }
  .card {
    position: absolute;
    top: 326px;
    width: 500px;
    height: 286px;
    background: var(--card-white);
    box-shadow: 0 6px 18px rgba(0,0,0,0.18);
    overflow: hidden;
  }
  .card--front { left: 70px; }
  .card--back  { left: 630px; }

  .logo {
    display: flex;
    align-items: center;
    gap: 8px;
    font-weight: 700;
    letter-spacing: 0.2px;
    color: var(--ink);
  }
  .logo__dot {
    width: 16px;
    height: 16px;
    border-radius: 50%;
    background: var(--brand-blue);
    flex: none;
  }
  .card--front .logo {
    position: absolute;
    left: 26px;
    top: 30px;
    font-size: 21px;
  }
  .card--back .logo {
    position: absolute;
    left: 0;
    right: 0;
    top: 34px;
    justify-content: center;
    font-size: 22px;
  }
  .card--back .note-rule {
    position: absolute;
    left: 40px;
    right: 40px;
    top: 84px;
    height: 2px;
    background: var(--brand-blue);
  }

  .address {
    position: absolute;
    left: 28px;
    top: 74px;
    font-size: 9.5px;
    line-height: 14px;
    color: var(--ink-soft);
  }
  .contact {
    position: absolute;
    right: 28px;
    top: 66px;
    text-align: right;
    color: var(--ink);
  }
  .contact__name {
    font-size: 15px;
    font-weight: 600;
    margin: 0;
  }
  .contact__title {
    font-size: 12px;
    color: var(--ink-soft);
    margin: 3px 0 14px;
  }
  .contact__line {
    display: flex;
    justify-content: flex-end;
    align-items: center;
    gap: 6px;
    font-size: 9.5px;
    line-height: 15px;
    color: var(--ink-soft);
  }
  .contact__line svg { width: 9px; height: 9px; fill: var(--ink-soft); }
  .wave {
    position: absolute;
    left: 0;
    bottom: 0;
    width: 500px;
    height: 286px;
  }
  .website {
    position: absolute;
    right: 26px;
    bottom: 14px;
    font-size: 10.5px;
    color: var(--on-dark);
    letter-spacing: 0.3px;
  }
</style>
</head>
<body>
<main class="stage">
  <section class="card card--front" aria-label="Card front">
    <svg class="wave" viewBox="0 0 500 286" aria-hidden="true">
      <path d="M0 178 C120 200 220 250 500 214 L500 232 C240 262 120 220 0 196 Z" fill="var(--swoosh-gray)"/>
      <path d="M0 204 C120 228 230 276 500 236 L500 286 L0 286 Z" fill="var(--brand-blue)"/>
      <path d="M0 240 C140 262 260 292 500 262 L500 286 L0 286 Z" fill="var(--brand-blue-dark)"/>
    </svg>
    <div class="logo"><span class="logo__dot"></span>bluepinelodge.net</div>
    <div class="address">
      418 Dunmere Lane<br>
      Suite 207<br>
      Spring, TX 77291
    </div>
    <div class="contact">
      <p class="contact__name">Morris Trulsow</p>
      <p class="contact__title">President</p>
      <div class="contact__line">024 615 3308
        <svg viewBox="0 0 10 10"><path d="M2 0.5 L4 2.5 L3 4 C3.8 5.6 4.6 6.4 6 7 L7.5 6 L9.5 8 L8 9.5 C4 9 1 6 0.5 2 Z"/></svg>
      </div>
      <div class="contact__line">024 615 3309
        <svg viewBox="0 0 10 10"><rect x="1" y="3" width="8" height="6" rx="1"/><rect x="3" y="0.5" width="4" height="3"/></svg>
      </div>
      <div class="contact__line">morris@bluepinelodge.net
        <svg viewBox="0 0 10 10"><rect x="0.5" y="2" width="9" height="6"/></svg>
      </div>
    </div>
    <div class="website">www.bluepinelodge.net</div>
  </section>

  <section class="card card--back" aria-label="Card back, space for a handwritten note">
    <div class="logo"><span class="logo__dot"></span>bluepinelodge.net</div>
    <div class="note-rule"></div>
  </section>
</main>
</body>
</html>
```